Northbound's green Wagon Van Decal

Good day,
I am looking for a decal or wrap for my work van. The name of the Business is Northbound’s Green Wagon, and we are a van rental company with a provided driver. We offer transport, delivery and expediting services to our customers.
The Van is a 2024 Vexa Cargoline 3400 159in wb ext. and its red.
I do not want a fully 360 top to bottom van decal just the region in green on both side of the van and in the back for the decal. See attached.
The following is text information that needs to be added on the decal.
- Name of the Business is Northbound’s Green Wagon
- Company motto: Your buddy behind the wheel
- Van Rental with driver
- Evenings and weekends.
The costumer can contact us by:
Email: Rosedale@northboundsgreenwagon.com
Phone or Text at: 555-274-9061
Keep in mind that the van is RED. If I cannot Invision what your wrap will look like on the Van there’s a high chance it won’t be chosen.
Thank you for your time.
Updates
Low design quality
Good day,
I have change the requirement of the project. it should be a lot more manageable and foster more creativity from designer.
Please have a look at the revise brief if you're interested.
Industry/Entity Type
Moving business
Look and feel
Each slider illustrates characteristics of the customer's brand and the style your logo design should communicate.

```html
<!DOCTYPE html>
<html lang="en">
<head>
<meta charset="utf-8">
<title>Northbound's Green Wagon – Van Side Decal</title>
<link rel="stylesheet" href="https://fonts.googleapis.com/css2?family=Poppins:wght@400;600;700&display=swap">
<style>
  :root {
    --van-red: #c8100f;
    --decal-white: #f4f4f4;
    --decal-edge: #b9b9b9;
    --ink: #111111;
    --brand-red: #cc1616;
    --rule-grey: #8d8d8d;
  }
  * { margin: 0; padding: 0; box-sizing: border-box; }
  html, body {
    width: 1200px;
    height: 1200px;
    overflow: hidden;
  }
  body {
    background: var(--van-red);
    font-family: "Poppins", sans-serif;
    position: relative;
  }
  .side-decal {
    position: absolute;
    left: 50px;
    top: 488px;
    width: 1100px;
    height: 224px;
    background: var(--decal-white);
    border-radius: 10px;
    box-shadow: inset 0 0 0 3px var(--decal-edge);
  }
  .decal-motto {
    position: absolute;
    left: 80px;
    top: 14px;
    font-size: 36px;
    font-weight: 400;
    letter-spacing: 2px;
    color: var(--brand-red);
    white-space: nowrap;
  }
  .decal-motto strong { font-weight: 700; }
  .decal-phone {
    position: absolute;
    left: 176px;
    top: 64px;
    font-size: 50px;
    font-weight: 700;
    color: var(--ink);
    letter-spacing: 1px;
    line-height: 1.1;
  }
  .decal-email {
    position: absolute;
    left: 178px;
    top: 125px;
    font-size: 20px;
    font-weight: 400;
    color: var(--ink);
  }
  .decal-services {
    position: absolute;
    left: 46px;
    top: 152px;
    display: flex;
    gap: 14px;
    list-style: none;
    font-size: 24px;
    font-weight: 700;
    color: var(--brand-red);
    white-space: nowrap;
  }
  .decal-services li::before {
    content: "";
    display: inline-block;
    width: 13px;
    height: 13px;
    margin-right: 9px;
    border-radius: 50%;
    background: var(--ink);
    vertical-align: 2px;
  }
  .decal-rule {
    position: absolute;
    left: 180px;
    top: 196px;
    width: 556px;
    height: 14px;
  }
  .brand-mark {
    position: absolute;
    left: 760px;
    top: -10px;
    width: 250px;
    height: 216px;
    display: flex;
    flex-direction: column;
    align-items: center;
    justify-content: center;
    gap: 12px;
    text-align: center;
  }
  .brand-dot {
    width: 46px;
    height: 46px;
    border-radius: 50%;
    background: var(--brand-red);
  }
  .brand-name {
    font-size: 26px;
    font-weight: 600;
    line-height: 1.15;
    color: var(--brand-red);
  }
</style>
</head>
<body>
  <section class="side-decal" aria-label="Van side decal">
    <p class="decal-motto">Your <strong>buddy</strong> behind the <strong>wheel</strong></p>
    <p class="decal-phone">555-274-9061</p>
    <p class="decal-email">Rosedale@northboundsgreenwagon.com</p>
    <ul class="decal-services">
      <li>Van Rental with driver</li>
      <li>Evenings and weekends</li>
    </ul>
    <svg class="decal-rule" viewBox="0 0 556 14" aria-hidden="true">
      <line x1="4" y1="7" x2="552" y2="7" stroke="#8d8d8d" stroke-width="3"/>
      <rect x="0" y="2" width="10" height="10" fill="#333"/>
      <rect x="546" y="2" width="10" height="10" fill="#333"/>
    </svg>
    <div class="brand-mark">
      <span class="brand-dot" aria-hidden="true"></span>
      <span class="brand-name">Northbound’s Green Wagon</span>
    </div>
  </section>
</body>
</html>
```